VORUN -Box for Tisanes( Tea made from Herbs & fruits)

We would like to start a new brand called " Vorun" which will have 7 variants of tisanes ( basically teas made from plant parts) . These are all colorful boxes and you could use the ingredient photos and put on the box. Each box will have 20 pyramid  tea bags
I have attached the
1) actual pic of the loose tea ( total 5 types)
2) We will pack this in Pyramid Bags. I have attached picture of the Pyramid bag packaging
3) Some ideas about how the box should look like ( from other brands)
4) there is also a key line to follow for the sizing
5) leave space for Nutritional information , ingredients etc

Online b2c

```html
<!DOCTYPE html>
<html lang="en">
<head>
<meta charset="utf-8">
<title>Vorun – Tisane Box Range</title>
<link href="https://fonts.googleapis.com/css2?family=DM+Sans:wght@700;800&family=Kaushan+Script&display=swap" rel="stylesheet">
<style>
  :root {
    --canvas: #ffffff;
    --ink: #111111;
    --lime: #b9e14c;
    --lime-deep: #9fcc35;
    --frame-line: #f6f2a0;
    --paper: #ffffff;
    --mint-top: #7fd9cc;
    --mint-bottom: #a6dfae;
    --lemon-top: #ead75c;
    --lemon-bottom: #dcd45a;
    --rose-top: #c9383f;
    --rose-bottom: #bf3940;
    --rose-pill: #c23a40;
    --herb-mint: #7d8a4e;
    --herb-lemon: #b9863c;
    --herb-rose: #a98560;
  }
  * { margin: 0; padding: 0; box-sizing: border-box; }
  html, body { width: 1000px; height: 1200px; overflow: hidden; background: var(--canvas); }
  .canvas { position: relative; width: 1000px; height: 1200px; font-family: "DM Sans", sans-serif; color: var(--ink); }

  .brand-mark { position: absolute; left: 38px; top: 38px; }
  .brand-mark .wordmark { font-size: 68px; font-weight: 800; letter-spacing: 1px; line-height: 1; }
  .brand-mark .tagline { font-size: 15.5px; font-weight: 700; margin-top: 10px; padding-left: 14px; }

  .box-stack { position: absolute; left: 337px; top: 140px; width: 315px; }
  .tea-box {
    position: relative; width: 315px; height: 322px; overflow: hidden;
    border-bottom: 1px solid rgba(0,0,0,0.08);
  }
  .tea-box .pattern-field { position: absolute; inset: 0; }
  .tea-box .lower-band {
    position: absolute; left: 0; right: 0; bottom: 0; height: 68px; background: var(--lime);
  }
  .tea-box .header-panel {
    position: absolute; left: 22px; right: 22px; top: 0; height: 112px;
    background: var(--lime); border-radius: 0 0 24px 24px;
  }
  .tea-box .header-frame {
    position: absolute; left: 32px; right: 32px; top: -2px; height: 102px;
    border: 2px solid var(--frame-line); border-top: none; border-radius: 0 0 20px 20px;
  }
  .tea-box .box-wordmark {
    position: absolute; left: 0; right: 0; top: 22px; text-align: center;
    font-size: 46px; font-weight: 800; line-height: 1; letter-spacing: 1px;
  }
  .tea-box .box-tagline {
    position: absolute; left: 0; right: 0; top: 74px; text-align: center;
    font-size: 11.5px; font-weight: 700;
  }
  .tea-box .ingredient-photo {
    position: absolute; left: 172px; top: 156px; width: 126px; height: 126px;
    border-radius: 50%; border: 6px solid var(--lime-deep);
  }
  .tea-box .variant-name {
    position: absolute; left: 10px; z-index: 2;
    font-family: "Kaushan Script", cursive;
    font-size: 21px; line-height: 1.2; color: var(--ink);
    text-shadow: 2px 0 0 #fff, -2px 0 0 #fff, 0 2px 0 #fff, 0 -2px 0 #fff,
                 2px 2px 0 #fff, -2px -2px 0 #fff, 2px -2px 0 #fff, -2px 2px 0 #fff;
  }
  .tea-box .variant-name--pill {
    left: 6px; padding: 2px 14px 4px 8px; font-size: 26px;
    background: var(--rose-pill); border: 2px solid var(--paper); border-radius: 20px;
  }

  .tea-box--mint .pattern-field { background: linear-gradient(180deg, var(--mint-top), var(--mint-bottom)); }
  .tea-box--mint .ingredient-photo { background: radial-gradient(circle, #9aa565, var(--herb-mint)); }
  .tea-box--lemon .pattern-field { background: linear-gradient(180deg, var(--lemon-top), var(--lemon-bottom)); }
  .tea-box--lemon .ingredient-photo { background: radial-gradient(circle, #d29c4e, var(--herb-lemon)); }
  .tea-box--rose .pattern-field { background: linear-gradient(180deg, var(--rose-top), var(--rose-bottom)); }
  .tea-box--rose .ingredient-photo { background: radial-gradient(circle, #c5a27a, var(--herb-rose)); }
</style>
</head>
<body>
<div class="canvas">

  <header class="brand-mark">
    <div class="wordmark">VORUN</div>
    <div class="tagline">Tea made from herbs &amp; fruits</div>
  </header>

  <main class="box-stack">
    <section class="tea-box tea-box--mint">
      <div class="pattern-field" role="img" aria-label="Teal leaf pattern background"></div>
      <div class="lower-band"></div>
      <div class="header-panel"></div>
      <div class="header-frame"></div>
      <div class="box-wordmark">VORUN</div>
      <div class="box-tagline">Tea made from herbs &amp; fruits</div>
      <div class="ingredient-photo" role="img" aria-label="Photo of loose mint tea leaves with a pyramid tea bag"></div>
      <div class="variant-name" style="top:226px;">Misty Meadow<br>Mint Bliss</div>
    </section>

    <section class="tea-box tea-box--lemon">
      <div class="pattern-field" role="img" aria-label="Yellow leaf pattern background"></div>
      <div class="lower-band"></div>
      <div class="header-panel"></div>
      <div class="header-frame"></div>
      <div class="box-wordmark">VORUN</div>
      <div class="box-tagline">Tea made from herbs &amp; fruits</div>
      <div class="ingredient-photo" role="img" aria-label="Photo of loose fruit and citrus peel tea with a pyramid tea bag"></div>
      <div class="variant-name" style="top:216px;">Sunny Zesty<br>&amp; Citrus</div>
    </section>

    <section class="tea-box tea-box--rose">
      <div class="pattern-field" role="img" aria-label="Red leaf pattern background"></div>
      <div class="lower-band"></div>
      <div class="header-panel"></div>
      <div class="header-frame"></div>
      <div class="box-wordmark">VORUN</div>
      <div class="box-tagline">Tea made from herbs &amp; fruits</div>
      <div class="ingredient-photo" role="img" aria-label="Photo of loose herbal tea with rose petals and a pyramid tea bag"></div>
      <div class="variant-name variant-name--pill" style="top:228px;">Glowbrew</div>
    </section>
  </main>

</div>
</body>
</html>
```